Corporate brochure design 4 pages

Hi,

We are a real estate company based in Europe.

We have almost finalized a rebranding.

We are developing a brand book guidelines (still on working process) to help you undertstand the look and feel of our new CI. I would like to receive proposals of design for a corporate brochure template. I need to receive the Indesign files with full ownership rights to be able to adapt all our documentation with this template.
Regarding the images, you can take gabaris on www.pelvaromedia.com. I will be able to take them afterwards.

There will be 4 pages. you will receive the 4 pages on pdf for your consideration with our (almost) actual layout.

- 1st page: cover
- 2nd page: company presentation in french and english
- 3rd page: some market data + graph
- 4th page: 2 retail centers presentation.

In the template, i need to have:
- the paragraph styles in order
- 2 different masters with top/bottom/page number aso.

Please feel free to ask any other questions.

best regards,
Updates

I would like to precise tha t we are active on the commercial real estate sector:

- office transactions (rent /sales)
- property management of administrative and business buildings
- Valuation of properties
- Capital markets (investment advices for selling building)

Industry/Entity Type

Real Estate

Colors

Designer to choose colors to be used in the design.

```html
<!DOCTYPE html>
<html lang="en">
<head>
<meta charset="utf-8">
<title>Halvern Commercial Real Estate – Brochure Cover</title>
<link rel="stylesheet" href="https://fonts.googleapis.com/css2?family=Arimo:wght@400;700&display=swap">
<style>
  :root {
    --orange: #f26722;
    --ink: #1f1f1f;
    --paper: #f3f3f3;
    --rule-dark: #222222;
    --rule-grey: #b9b9b9;
    --bullet: #8c8c8c;
    --white: #ffffff;
    --photo-light: #eef4f4;
    --photo-mid: #9fc3c7;
    --photo-deep: #3f6f78;
  }
  * { box-sizing: border-box; margin: 0; padding: 0; }
  html, body { width: 875px; height: 1200px; overflow: hidden; background: var(--white); }
  body { font-family: "Arimo", Arial, sans-serif; }

  .cover { position: relative; width: 875px; height: 1200px; background: var(--paper); }

  .cover-photo {
    position: absolute; left: 0; top: 0; width: 875px; height: 825px;
    background:
      linear-gradient(115deg, transparent 0 8%, rgba(63,111,120,.55) 8% 40%, transparent 40%),
      radial-gradient(ellipse at 30% 25%, var(--photo-light) 0%, rgba(238,244,244,.6) 30%, transparent 60%),
      linear-gradient(160deg, var(--photo-light) 0%, var(--photo-mid) 55%, var(--photo-deep) 100%);
  }

  .rule { position: absolute; left: 0; width: 875px; }
  .rule-dark { background: var(--rule-dark); height: 5px; }
  .rule-grey { background: linear-gradient(90deg, var(--rule-grey), #e6e6e6 50%, var(--rule-grey)); height: 3px; }

  .brand {
    position: absolute; left: 0; top: 836px; width: 875px; height: 142px;
    background: linear-gradient(180deg, #fafafa, #ededed);
    text-align: center;
  }
  .brand-name {
    position: absolute; left: 0; right: 0; top: 28px;
    font-weight: 700; font-size: 72px; line-height: 1; letter-spacing: -3px;
    color: var(--ink);
  }
  .brand-tagline {
    position: absolute; left: 0; right: 0; top: 106px;
    font-size: 19px; letter-spacing: 4.5px; color: var(--orange);
  }

  .services {
    position: absolute; left: 0; top: 989px; width: 875px; height: 148px;
    background: var(--orange); color: var(--white);
  }
  .services-title {
    position: absolute; left: 0; right: 0; top: 14px;
    text-align: center; font-size: 22.5px; letter-spacing: 0.2px;
  }
  .services-divider { position: absolute; left: 436px; top: 64px; width: 1px; height: 76px; background: var(--white); }
  .service { position: absolute; font-size: 15.5px; line-height: 21px; }
  .service-left { right: 459px; text-align: right; }
  .service-right { left: 458px; }
  .service::after, .service::before { }
  .dot {
    position: absolute; width: 8px; height: 8px; border-radius: 50%;
    background: var(--bullet); border: 2px solid var(--white);
  }

  .footer {
    position: absolute; left: 0; top: 1148px; width: 875px; height: 33px;
    background: var(--paper);
    display: flex; align-items: center; justify-content: center; gap: 4px;
  }
  .footer-url { font-size: 13px; letter-spacing: 5px; color: var(--ink); }
  .footer-base {
    position: absolute; left: 0; top: 1181px; width: 875px; height: 19px;
    background: linear-gradient(90deg, #1a1a1a, #4a4a4a 50%, #1a1a1a);
  }
</style>
</head>
<body>
<main class="cover">
  <div class="cover-photo" role="img" aria-label="Upward view of glass office towers against a bright sky, cool teal tones"></div>

  <div class="rule rule-dark" style="top:826px"></div>
  <div class="rule rule-grey" style="top:832px"></div>

  <section class="brand">
    <h1 class="brand-name">HALVERN</h1>
    <p class="brand-tagline">COMMERCIAL REAL ESTATE</p>
  </section>

  <div class="rule rule-dark" style="top:978px"></div>
  <div class="rule rule-grey" style="top:984px"></div>

  <section class="services">
    <h2 class="services-title" style="font-weight:400">WE ARE ACTIVE ON THE COMMERCIAL REAL ESTATE SECTOR :</h2>
    <div class="services-divider"></div>

    <p class="service service-left" style="top:57px">Office transactions (rent /sales)</p>
    <span class="dot" style="left:423px;top:64px"></span>
    <span class="dot" style="left:445px;top:64px"></span>
    <p class="service service-right" style="top:57px">Valuation of properties</p>

    <p class="service service-left" style="top:90px">Property management of<br>administrative and business buildings</p>
    <span class="dot" style="left:423px;top:97px"></span>
    <span class="dot" style="left:445px;top:97px"></span>
    <p class="service service-right" style="top:90px">Capital markets<br>(investment advices for selling building)</p>
  </section>

  <div class="rule rule-grey" style="top:1138px;height:4px"></div>
  <div class="rule rule-dark" style="top:1142px;height:4px"></div>

  <footer class="footer">
    <svg width="10" height="10" viewBox="0 0 10 10" aria-hidden="true">
      <circle cx="5" cy="5" r="4.3" fill="none" stroke="#f26722" stroke-width="1.2"/>
      <ellipse cx="5" cy="5" rx="1.8" ry="4.3" fill="none" stroke="#f26722" stroke-width="0.9"/>
      <line x1="0.7" y1="5" x2="9.3" y2="5" stroke="#f26722" stroke-width="0.9"/>
    </svg>
    <span class="footer-url">www.halverngroup.net</span>
  </footer>
  <div class="footer-base"></div>
</main>
</body>
</html>
```